Agricultural Commodities Specialist Needs a Business Card Design

Business owner Rob Tenwick, need a business card design for his company based in Brisbane, Australia called "RT Harvestline Pty Ltd".
Rob is an Agricultural Commodities Specialist:
-Specialising in Domestic and Export of Cotton,Cottonseed and Grains.
-Extensive experience in exporting into Asia especially China.
-Buyers agent for one of China's largest spinning mills.
-Capital raising from foreign investors into Australian agriculture.
-Agricultural marketing strategies for corporate and family farms.
-Importer of niche products from China.
-Array of contacts in agriculture and manufacturing in China.

Rob would like a professional business card with his company name "RT Harvestline" on the front of his business card - with contact details on the back. Preferably black and white colours.

CONTACT DETAILS THAT NEED TO BE INCLUDED:

Rob Tenwick
Mobile: 0437 615 249

Po Box 579
Kelwyn Park QLD 4187

Email: rob@rtharvestline.com
website: www.rtharvestlin.com

```html
<!DOCTYPE html>
<html lang="en">
<head>
<meta charset="utf-8">
<title>RT Harvestline – Business Card</title>
<link rel="stylesheet" href="https://fonts.googleapis.com/css2?family=Alegreya:wght@400&family=Delius&display=swap">
<style>
  :root {
    --backdrop: #c9c9c7;
    --card-black: #0b0b0b;
    --card-glow: #262626;
    --ink-white: #f4f4f4;
    --ink-grey: #9a9a9a;
    --rule: #d8d8d8;
  }
  * { margin: 0; padding: 0; box-sizing: border-box; }
  html, body { width: 1200px; height: 725px; overflow: hidden; }
  body {
    background: var(--backdrop);
    display: flex;
    align-items: center;
    justify-content: center;
    gap: 50px;
  }
  .card {
    width: 530px;
    height: 303px;
    background: radial-gradient(ellipse at 50% 35%, var(--card-glow) 0%, var(--card-black) 70%);
    border-radius: 3px;
    box-shadow: 0 6px 18px rgba(0,0,0,.25);
    position: relative;
    overflow: hidden;
  }
  .brand {
    font-family: "Alegreya", serif;
    font-weight: 400;
    color: var(--ink-white);
    display: flex;
    align-items: center;
    gap: 12px;
    white-space: nowrap;
  }
  .brand-dot {
    width: 14px; height: 14px;
    border-radius: 50%;
    background: currentColor;
    flex: none;
  }
  .card-front { display: flex; align-items: center; justify-content: center; }
  .card-front .brand { font-size: 44px; }

  .card-back { display: flex; }
  .back-brand {
    width: 50%;
    display: flex;
    align-items: center;
    justify-content: center;
  }
  .back-brand .brand { font-size: 30px; color: var(--ink-grey); gap: 9px; }
  .back-brand .brand-dot { width: 10px; height: 10px; }
  .divider {
    width: 1px;
    background: var(--rule);
    margin: 24px 0;
  }
  .contact {
    flex: 1;
    padding: 30px 0 0 30px;
    color: var(--ink-white);
    font-family: "Delius", sans-serif;
  }
  .contact-name {
    font-family: "Alegreya", serif;
    font-size: 28px;
    letter-spacing: .3px;
    margin-bottom: 8px;
  }
  .contact-row {
    display: flex;
    align-items: center;
    gap: 10px;
    font-size: 15px;
    line-height: 1.2;
    margin-bottom: 7px;
    white-space: nowrap;
  }
  .contact-row svg { width: 18px; height: 18px; flex: none; fill: var(--ink-white); }
  .contact-phone { font-size: 22px; margin-bottom: 10px; }
  .contact-phone svg { width: 16px; height: 28px; }
  .contact-rule {
    width: 165px;
    height: 1px;
    background: var(--rule);
    margin: 0 0 14px 8px;
  }
  .contact-plain { padding-left: 28px; }
</style>
</head>
<body>

  <section class="card card-front">
    <div class="brand"><span class="brand-dot"></span>RT Harvestline</div>
  </section>

  <section class="card card-back">
    <div class="back-brand">
      <div class="brand"><span class="brand-dot"></span>RT Harvestline</div>
    </div>
    <div class="divider"></div>
    <div class="contact">
      <p class="contact-name">Rob Tenwick</p>
      <p class="contact-row contact-phone">
        <svg viewBox="0 0 16 28" aria-hidden="true"><path d="M3 0h10a3 3 0 0 1 3 3v22a3 3 0 0 1-3 3H3a3 3 0 0 1-3-3V3a3 3 0 0 1 3-3zm-1 4v18h12V4zm6 19.5a1.5 1.5 0 1 0 0 3 1.5 1.5 0 0 0 0-3z"/></svg>
        0437 615 249
      </p>
      <div class="contact-rule"></div>
      <p class="contact-row">
        <svg viewBox="0 0 20 20" aria-hidden="true"><path d="M5 2h10a5 5 0 0 1 5 5v6H9V7a4 4 0 0 0-4-4zM4 4a4 4 0 0 1 4 4v5H0V8a4 4 0 0 1 4-4zm2 10h4v6H6z"/></svg>
        Po Box 579
      </p>
      <p class="contact-row contact-plain">Kelwyn Park QLD 4187</p>
      <p class="contact-row">
        <svg viewBox="0 0 20 20" aria-hidden="true"><path d="M0 9 20 1l-4 18-6-5-3 4v-6l9-9-11 7z"/></svg>
        rob@rtharvestline.com
      </p>
      <p class="contact-row">
        <svg viewBox="0 0 20 20" aria-hidden="true"><circle cx="10" cy="10" r="10"/><text x="10" y="12.5" font-size="6" font-family="sans-serif" font-weight="700" text-anchor="middle" fill="#0b0b0b">www</text></svg>
        www.rtharvestlin.com
      </p>
      <p class="contact-row contact-plain">www.rtharvestlin.com</p>
    </div>
  </section>

</body>
</html>
```